Brightpath Medical Exercise, LLC specializes in post rehab medical exercise for clients who have been discharged from physical therapy and/or other medical services and are in need of continued cardiovascular, strength, flexibility, endurance training and management of their medical conditions. We strive to bridge the gap between healthcare and fitness by staying in communication with the referring physician and /or physical therapist with updated progress notes to follow each clients progression, making sure each client is appropriate for exercise and identifying any red flags throughout the initial assessment and screening of the client, and referring those clients back to the physician and/or therapist when necessary.
Colors
Designer to choose colors to be used in the design.
Requirements
Must have
- Pictures of a trainer working with a client one on one during exercise, and group exercise
Nice to have
- Pictures that portray the bridge between healthcare and fitness
Should not have
- Cursive writing

```html
<!DOCTYPE html>
<html lang="en">
<head>
<meta charset="utf-8">
<title>Brightpath Medical Exercise – Rack Cards</title>
<link rel="stylesheet" href="https://fonts.googleapis.com/css2?family=Arvo:wght@400;700&family=Roboto+Slab:wght@300;400;500&display=swap">
<style>
  :root {
    --navy: #11142f;
    --coral: #ef5a4f;
    --white: #ffffff;
    --band: #ebebef;
    --page: #e7e7e7;
    --heading: "Arvo", Georgia, serif;
    --body: "Roboto Slab", "Arvo", Georgia, serif;
  }
  * { margin: 0; padding: 0; box-sizing: border-box; }
  html, body { width: 1200px; height: 1200px; overflow: hidden; background: var(--page); }
  .canvas { position: relative; width: 1200px; height: 1200px; }

  .card { position: absolute; width: 501px; height: 1092px; background: var(--white); overflow: hidden; }
  .card--front { left: 91px; top: 54px; }
  .card--back { left: 617px; top: 52px; }
  .card__shapes { position: absolute; inset: 0; }
  .abs { position: absolute; }

  /* Front */
  .headline { left: 52px; top: 500px; font-family: var(--heading); font-weight: 700; color: var(--coral); font-size: 33px; line-height: 39px; }
  .pill { left: 50px; top: 688px; height: 28px; padding: 0 12px 0 10px; border-radius: 14px; background: var(--coral); color: var(--white); font-family: var(--heading); font-weight: 700; font-size: 19.5px; line-height: 28px; }
  .services { left: 54px; top: 733px; list-style: none; color: var(--white); font-family: var(--body); font-weight: 300; font-size: 18px; line-height: 23.5px; }
  .services li { position: relative; padding-left: 32px; margin-bottom: 8px; }
  .services svg { position: absolute; left: 0; top: 5px; }

  .contact { left: 59px; font-family: var(--heading); font-weight: 700; font-size: 22px; line-height: 26px; }
  .contact__phone { color: var(--coral); }
  .contact__web { color: var(--navy); }

  .brand { width: 110px; text-align: center; font-family: var(--body); font-weight: 500; font-size: 9px; line-height: 11px; color: var(--navy); letter-spacing: 0.2px; }

  /* Back */
  .quote { left: 0; width: 501px; top: 62px; text-align: center; color: var(--white); font-family: var(--body); font-weight: 300; font-size: 24px; line-height: 34.5px; }
  .quote__author { left: 0; width: 501px; top: 174px; text-align: center; color: var(--coral); font-family: var(--heading); font-weight: 700; font-size: 23px; }
  .offer { left: 42px; top: 318px; color: var(--coral); font-family: var(--heading); font-weight: 700; font-size: 20.5px; line-height: 26px; }
  .photo-circle { left: 293px; top: 240px; width: 175px; height: 175px; border-radius: 50%; background: radial-gradient(circle at 60% 40%, #cfe2f5 0%, #7fb0e3 45%, #2f67b3 100%); border: 3px solid var(--navy); }

  .conditions { left: 31px; top: 464px; width: 442px; font-family: var(--body); font-weight: 400; font-size: 15px; color: var(--navy); letter-spacing: -0.5px; }
  .conditions__row { display: grid; grid-template-columns: 214px 1fr; height: 27px; align-items: center; padding-left: 11px; line-height: 19px; }
  .conditions__row--tall { height: 47px; }
  .conditions__row:nth-child(odd) { background: var(--band); }
  .conditions__row:nth-child(odd) span { font-weight: 500; }
</style>
</head>
<body>
<div class="canvas">

  <!-- Front card -->
  <section class="card card--front">
    <svg class="card__shapes" width="501" height="1092" viewBox="0 0 501 1092">
      <defs>
        <linearGradient id="deckTone" x1="0" y1="0" x2="0" y2="1">
          <stop offset="0" stop-color="#1d2620"/>
          <stop offset="0.45" stop-color="#3a3128"/>
          <stop offset="0.6" stop-color="#b89c84"/>
          <stop offset="1" stop-color="#d8c3ad"/>
        </linearGradient>
      </defs>
      <polygon points="0,0 501,0 501,492 0,443" fill="url(#deckTone)" role="img" aria-label="Photo of blue dumbbells and a water bottle on a wooden deck"/>
      <polygon points="0,443 501,478 501,496 0,463" fill="var(--coral)"/>
      <polygon points="0,463 501,496 501,975 0,933" fill="var(--navy)"/>
      <polygon points="0,933 501,975 501,990 0,952" fill="var(--coral)"/>
      <circle cx="392" cy="958" r="68" fill="var(--white)" stroke="var(--coral)" stroke-width="3"/>
    </svg>

    <h1 class="abs headline">Getting You<br>Back To Function<br>As Quickly and Safely<br>As Possible</h1>
    <div class="abs pill">Our Products and Services</div>
    <ul class="abs services">
      <li><svg width="20" height="20" viewBox="0 0 20 20"><circle cx="10" cy="10" r="9" fill="var(--coral)"/><path d="M5.5 10.2l3 3 6-6.5" fill="none" stroke="var(--white)" stroke-width="2.2"/></svg>Initial Assessment and<br>Functional Screening</li>
      <li><svg width="20" height="20" viewBox="0 0 20 20"><circle cx="10" cy="10" r="9" fill="var(--coral)"/><path d="M5.5 10.2l3 3 6-6.5" fill="none" stroke="var(--white)" stroke-width="2.2"/></svg>One-On-One supervised<br>post rehab exercise</li>
      <li><svg width="20" height="20" viewBox="0 0 20 20"><circle cx="10" cy="10" r="9" fill="var(--coral)"/><path d="M5.5 10.2l3 3 6-6.5" fill="none" stroke="var(--white)" stroke-width="2.2"/></svg>Online consultation with<br>individualized home<br>exercise program</li>
    </ul>

    <p class="abs contact contact__phone" style="top:990px">Call us 555 01 23</p>
    <p class="abs contact contact__web" style="top:1021px">Website to come</p>
    <p class="abs brand" style="left:337px; top:947px">BRIGHTPATH<br>MEDICAL EXERCISE</p>
  </section>

  <!-- Back card -->
  <section class="card card--back">
    <svg class="card__shapes" width="501" height="1094" viewBox="0 0 501 1094">
      <polygon points="0,0 501,0 501,315 0,266" fill="var(--navy)"/>
      <polygon points="0,266 501,315 501,322 0,287" fill="var(--coral)"/>
      <polygon points="0,936 330,958 330,976 0,955" fill="var(--coral)"/>
      <polygon points="455,980 501,984 501,990 455,987" fill="var(--coral)"/>
      <circle cx="396" cy="973" r="62" fill="var(--white)" stroke="var(--coral)" stroke-width="3"/>
    </svg>

    <blockquote class="abs quote">“Exercise is the key to<br>long-term management of<br>most medical conditions”</blockquote>
    <p class="abs quote__author">Daniel R Hayes, PhD, PT</p>

    <div class="abs photo-circle" role="img" aria-label="Photo of a therapist guiding a client's leg exercise"></div>
    <h2 class="abs offer">We offer<br>management of<br>the following<br>conditions and more:</h2>

    <div class="abs conditions">
      <div class="conditions__row"><span>Diabetes</span><span>AC Joint Separation</span></div>
      <div class="conditions__row"><span>Hypertension</span><span>Fibromyalgia</span></div>
      <div class="conditions__row"><span>ACL Rupture</span><span>Spondylothesis</span></div>
      <div class="conditions__row"><span>Ankle Fracture</span><span>Parkinson’s Disease</span></div>
      <div class="conditions__row"><span>Bicipital Tendonitis</span><span>Tibial Plateau Fracture</span></div>
      <div class="conditions__row conditions__row--tall"><span>Total Hip Replacement</span><span>Tennis Elbow/<br>Golfer’s Elbow</span></div>
      <div class="conditions__row conditions__row--tall"><span>Total Knee Replacement</span><span>Carpal Tunnel<br>Syndrome</span></div>
      <div class="conditions__row"><span>Spinal Stenosis</span><span>Total Shoulder Replacement</span></div>
      <div class="conditions__row"><span>Multiple Sclerosis</span><span>Bicipital Tendonitis</span></div>
      <div class="conditions__row"><span>Shoulder Dislocation</span><span>Patello-Femoral Syndrome</span></div>
      <div class="conditions__row"><span>Scoliosis</span><span>Rotator Cuff Syndrome</span></div>
      <div class="conditions__row"><span>Osteoporosis</span><span>Cervical Strain</span></div>
      <div class="conditions__row"><span>Osteoarthritis</span><span>Impingement Syndrome</span></div>
      <div class="conditions__row"><span>Cervical disc herniation</span><span>Laminectomy</span></div>
    </div>

    <p class="abs contact contact__phone" style="top:993px">Call us 555 01 23</p>
    <p class="abs contact contact__web" style="top:1024px">Website to come</p>
    <p class="abs brand" style="left:341px; top:962px">BRIGHTPATH<br>MEDICAL EXERCISE</p>
  </section>

</div>
</body>
</html>
```